Zielgruppe
Beamer Vermietung
Aufgabenstellung
Erstellung 2 professionell aussehender Webseiten.
Projektor-Verleih-Region-Wendlar.de
sowie
Projektor-Verleih-Region-Haselfurtheim.de
Die Seiten sind aktuell im Betrieb, aber haben ein sehr veraltetes Design.
Die Seiten können ähnlich aussehen, sollten aber etwas unterschiedlich sein, damit sie für den Kunden leicht anders aussehen.
Wichtig ist, dass alle Seiten, inklusive Startseite, Unterseiten und Links designed werden und das dieses Design in die bestehende Wordpress Installation eingepflegt wird.
Es ist also notwendig, gute Wordpress Kenntnisse zu haben um dann auch zwei fertige Wordpress Seiten liefern zu können.

```html
<!DOCTYPE html>
<html lang="de">
<head>
<meta charset="utf-8">
<title>Projektor-Verleih Region Wendlar</title>
<link href="https://fonts.googleapis.com/css2?family=Roboto:wght@300;400;500;700;900&family=Roboto+Condensed:wght@400&display=swap" rel="stylesheet">
<style>
:root{
  --blue:#1f62a0;
  --blue-dark:#1b5590;
  --blue-footer:#2170ad;
  --yellow:#f3c31a;
  --navy:#1c3a5c;
  --grey-bar:#ececec;
  --grey-band:#efefef;
  --text-grey:#6d6d6d;
  --white:#fff;
}
*{margin:0;padding:0;box-sizing:border-box}
html,body{width:763px;height:1200px;overflow:hidden;background:var(--white);font-family:'Roboto',sans-serif}
.page{position:relative;width:763px;height:1200px}
.abs{position:absolute}
.topbar{left:0;top:0;width:763px;height:19px;background:var(--grey-bar);border-bottom:1px solid #dcdcdc}
.topbar .url{left:104px;top:4px;font-size:7px;color:#555}
.social{top:5px;width:10px;height:10px;border-radius:50%;background:var(--navy)}
.site-title{left:101px;top:29px;font-family:'Roboto Condensed',sans-serif;font-size:18.5px;color:var(--blue)}
.header-links{top:35px;font-size:8.5px;font-weight:500;color:var(--navy)}
.nav{left:0;top:64px;width:763px;height:31px;background:var(--blue)}
.nav a{position:absolute;top:0;height:31px;line-height:31px;font-size:9px;font-weight:500;color:var(--white);text-decoration:none}
.nav a.active{background:var(--yellow);color:var(--navy);padding:0 8px}
.hero{left:0;top:95px;width:763px;height:293px;background:linear-gradient(100deg,#6f89a6 0%,#8aa0b7 40%,#9aa7b2 60%,#8f98a3 80%,#b4aa9f 100%)}
.hero-line{left:102px;top:163px;width:17px;height:2px;background:var(--yellow)}
.hero-title{left:102px;top:167px;font-size:29px;font-weight:700;line-height:35px;color:var(--white);white-space:nowrap}
.hero-sub{left:102px;top:237px;font-size:16px;font-weight:500;color:var(--white)}
.btn{background:var(--yellow);color:var(--navy);border-radius:12px;font-weight:500;text-align:center}
.btn-contact{left:103px;top:295px;width:90px;height:23px;line-height:23px;font-size:9px;font-weight:700}
.band{left:0;top:388px;width:763px;height:53px;background:var(--grey-band)}
.band-text{left:113px;top:404px;font-size:17.5px;font-weight:700;color:var(--blue);white-space:nowrap}
.price{display:inline-block;position:relative;color:var(--blue)}
.price::before{content:"";position:absolute;left:-3px;top:-9px;width:38px;height:38px;border-radius:50%;background:var(--yellow);z-index:-1}
.intro{left:0;top:460px;width:763px;text-align:center;font-size:18.5px;font-weight:300;line-height:24px;color:var(--blue)}
.offer h2{font-size:22px;font-weight:700;color:var(--blue);line-height:27px}
.offer p{font-size:22px;font-weight:300;color:var(--text-grey);line-height:28px}
.offer p.model{font-size:21px}
.btn-more{width:71px;height:24px;line-height:24px;font-size:9px}
.product-photo{background:radial-gradient(ellipse at 50% 50%,#9ea1a5 0%,#c9cbcd 50%,#fff 75%)}
.footer{left:0;top:1062px;width:763px;height:108px;background:linear-gradient(120deg,#1f69a8 0%,#2373b0 45%,#1d62a0 70%,#2170ad 100%)}
.footer-cta{left:100px;top:1100px;font-size:26px;font-weight:500;color:var(--yellow)}
.footer-tel{left:486px;top:1106px;font-size:20px;font-weight:300;color:var(--white)}
.copyright{left:0;top:1170px;width:763px;height:30px;background:var(--blue-dark);text-align:center;line-height:30px;font-size:7px;color:var(--white)}
</style>
</head>
<body>
<div class="page">
  <div class="abs topbar">
    <span class="abs url">www.projektor-verleih-region-wendlar.de</span>
  </div>
  <span class="abs social" style="left:589px;background:var(--yellow)"></span>
  <span class="abs social" style="left:608px"></span>
  <span class="abs social" style="left:627px"></span>
  <span class="abs social" style="left:646px"></span>

  <div class="abs site-title">Projektor Verleih zu Günstigen Konditionen</div>
  <svg class="abs" style="left:516px;top:36px" width="12" height="9" viewBox="0 0 12 9"><rect x="0.5" y="0.5" width="11" height="8" fill="none" stroke="#1c3a5c"/><path d="M0.5 0.5 L6 5 L11.5 0.5" fill="none" stroke="#1c3a5c"/></svg>
  <span class="abs header-links" style="left:535px">Kontakt / Anreise</span>
  <span class="abs header-links" style="left:616px">Impressum</span>

  <nav class="abs nav">
    <a class="active" style="left:103px">Startseite</a>
    <a style="left:162px">Beamer mieten</a>
    <a style="left:237px">HD-Beamer mieten</a>
    <a style="left:329px">Full HD-Beamer</a>
    <a style="left:406px">Leinwand mieten</a>
    <a style="left:489px">Reservierung</a>
    <a style="left:556px">Preisliste</a>
    <a style="left:606px">Datenschutz</a>
  </nav>

  <div class="abs hero" role="img" aria-label="Foto eines Beamers auf einem Holztisch vor unscharfem Publikum"></div>
  <div class="abs hero-line"></div>
  <h1 class="abs hero-title">&nbsp;! Beamer mieten zu<br>TOP-Konditionen !</h1>
  <div class="abs hero-sub">NEU: Jetzt auch HD-Beamer!</div>
  <div class="abs btn btn-contact">KONTAKT</div>

  <div class="abs band"></div>
  <svg class="abs" style="left:72px;top:402px" width="30" height="26" viewBox="0 0 30 26"><circle cx="9" cy="17" r="8" fill="#f3c31a"/><circle cx="26" cy="5" r="3.5" fill="#1c3a5c"/></svg>
  <div class="abs band-text" style="z-index:1">Beamer-Vermietung im Raum Wendlar / Brückstein&nbsp; für nur <span class="price">€30</span> / Tag</div>

  <div class="abs intro">Jetzt neu: HD-Beamer für das<br>perfekte Bilderlebnis zu günstigen Konditionen!</div>

  <section class="abs offer" style="left:104px;top:553px">
    <h2>Beamer mieten</h2>
    <p>Informationen zum Modell:<br>Beamer Modell Lumora LX410</p>
  </section>
  <div class="abs btn btn-more" style="left:103px;top:648px">Weiterlesen</div>
  <div class="abs product-photo" style="left:447px;top:538px;width:218px;height:147px" role="img" aria-label="Produktfoto Beamer Lumora LX410, dunkelgrau"></div>

  <div class="abs product-photo" style="left:103px;top:707px;width:208px;height:105px" role="img" aria-label="Produktfoto HD-Beamer Vantrix V720, silbern"></div>
  <section class="abs offer" style="left:338px;top:714px">
    <h2>HD Beamer mieten</h2>
    <p>Informationen zum Modell:</p>
    <p class="model">HD-Beamer Modell Vantrix V720</p>
  </section>
  <div class="abs btn btn-more" style="left:339px;top:803px">Weiterlesen</div>

  <section class="abs offer" style="left:104px;top:871px">
    <h2>Full-HD Beamer mieten</h2>
    <p>Informationen zum Modell:</p>
    <p class="model" style="font-size:18px">Full-HD-Beamer Modell Optiven HD24-LX</p>
  </section>
  <div class="abs btn btn-more" style="left:103px;top:966px">Weiterlesen</div>
  <div class="abs product-photo" style="left:443px;top:868px;width:220px;height:122px" role="img" aria-label="Produktfoto Full-HD-Beamer Optiven HD24-LX, weiß"></div>

  <footer>
    <div class="abs footer"></div>
    <div class="abs footer-cta">Reservieren oder Buchen</div>
    <svg class="abs" style="left:454px;top:1110px" width="22" height="16" viewBox="0 0 22 16"><path d="M1 5 C1 1 21 1 21 5 L21 7 L16 7 L16 4 L6 4 L6 7 L1 7 Z" fill="#f3c31a"/><path d="M5 8 L17 8 L20 15 L2 15 Z" fill="#f3c31a"/><circle cx="11" cy="11.5" r="2" fill="#2170ad"/></svg>
    <div class="abs footer-tel">Tel: 0163 / 5820417</div>
    <div class="abs copyright">Copyright © 2020.&nbsp; Projektor-Verleih-Region-Wendlar.de</div>
  </footer>
</div>
</body>
</html>
```